Managed Service Provider need new business cards

We are a small Maanged Service Provider of IT Services and need a new fresh design for our business cards. We want something impossible, fun and professional :)
Our services has a large range, but we are always fun and make sure our customers both get their issue sorted and also feel like they are "catching up with an old friend".
All our cards in the past has always been all black, with red and we need something fresher.
The back of card, we would like just a small list of what we do i think, but if someone has a better idea, please do something cool with the back of the card:
Managed IT Services
Productivity Solutions
Data Backup and Recovery
IT System Maintenance
Managed IT Security
More details can be found on our website tqnetworks.com.au
Industry/Entity Type
It Company
Contact Information for Business Card
Name: Dwayne Falstrup
Title: Director
Phone: 03 6193 4827
Mobile: 0412 587 239
Email: dwayne@tqnetworks.com.au
Web: www.tqnetworks.com.au

```html
<!DOCTYPE html>
<html lang="en">
<head>
<meta charset="UTF-8">
<title>TQ Networks — Business Cards</title>
<link href="https://fonts.googleapis.com/css2?family=Arimo:wght@400;700&display=swap" rel="stylesheet">
<style>
  :root {
    --page: #d9d6d2;
    --card: #1c1c1d;
    --card-edge: #111112;
    --red: #e3151d;
    --white: #ffffff;
    --emboss: #2b2b2c;
  }
  * { box-sizing: border-box; margin: 0; padding: 0; }
  html, body {
    width: 1200px; height: 716px; overflow: hidden;
    background: var(--page);
    font-family: "Arimo", Arial, sans-serif;
  }
  .canvas { position: relative; width: 1200px; height: 716px; }
  .card {
    position: absolute; width: 540px; height: 309px;
    background: var(--card);
    box-shadow: 0 10px 24px rgba(0,0,0,.35);
    overflow: hidden;
  }
  /* Back of card */
  .card-back { left: 40px; top: 70px; }
  .back-brand {
    position: absolute; left: 0; right: 0; top: 78px;
    text-align: center; font-weight: 700; font-size: 46px;
    letter-spacing: 1px; color: var(--emboss); text-transform: uppercase;
  }
  .service-list {
    position: absolute; left: 0; right: 0; top: 200px;
    text-align: center; color: var(--white); font-size: 13px; line-height: 22px;
  }
  .service-list .dot { color: var(--red); margin: 0 5px; }

  /* Front of card */
  .card-front { left: 620px; top: 337px; }
  .brand {
    position: absolute; left: 118px; top: 52px;
    display: flex; align-items: center; gap: 10px;
  }
  .brand-mark { width: 26px; height: 26px; border-radius: 50%; background: var(--white); }
  .brand-name {
    color: var(--red); font-weight: 700; font-size: 34px;
    text-transform: uppercase; letter-spacing: .5px;
  }
  .divider {
    position: absolute; left: 70px; top: 150px; width: 400px; height: 1px;
    background: var(--red);
  }
  .contact-list {
    position: absolute; left: 34px; top: 164px; list-style: none;
    color: var(--white); font-size: 13px; line-height: 21px;
  }
  .contact-list li { display: flex; align-items: center; gap: 7px; }
  .contact-list svg { width: 11px; height: 11px; fill: var(--red); flex: none; }
  .person {
    position: absolute; right: 52px; top: 206px; text-align: right;
  }
  .person-name {
    color: var(--red); font-weight: 700; font-size: 22px;
    text-transform: uppercase; letter-spacing: .5px;
  }
  .person-title { color: var(--white); font-size: 14px; margin-top: 4px; }
  .accent-bar {
    position: absolute; right: 28px; top: 212px; width: 12px; height: 46px;
    background: var(--red);
  }
</style>
</head>
<body>
<main class="canvas">

  <section class="card card-back" aria-label="Back of business card">
    <div class="back-brand">TQ Networks</div>
    <p class="service-list">
      Managed IT Services<span class="dot">•</span>Data Backup and Recovery<br>
      Productivity Solutions<span class="dot">•</span>IT System Maintenance<span class="dot">•</span>Managed IT Security
    </p>
  </section>

  <section class="card card-front" aria-label="Front of business card">
    <div class="brand">
      <span class="brand-mark"></span>
      <span class="brand-name">TQ Networks</span>
    </div>
    <div class="divider"></div>

    <ul class="contact-list">
      <li>
        <svg viewBox="0 0 24 24" aria-hidden="true"><path d="M6.6 10.8a15 15 0 0 0 6.6 6.6l2.2-2.2c.3-.3.7-.4 1-.2 1.1.4 2.3.6 3.6.6.6 0 1 .4 1 1V20c0 .6-.4 1-1 1A17 17 0 0 1 3 4c0-.6.4-1 1-1h3.5c.6 0 1 .4 1 1 0 1.3.2 2.5.6 3.6.1.3 0 .7-.2 1z"/></svg>
        03 6193 4827
      </li>
      <li>
        <svg viewBox="0 0 24 24" aria-hidden="true"><path d="M7 1h10a2 2 0 0 1 2 2v18a2 2 0 0 1-2 2H7a2 2 0 0 1-2-2V3a2 2 0 0 1 2-2zm0 3v14h10V4zm5 15.5a1 1 0 1 0 0 2 1 1 0 0 0 0-2z"/></svg>
        0412 587 239
      </li>
      <li>
        <svg viewBox="0 0 24 24" aria-hidden="true"><path d="M2 5h20v14H2zm2 2v.4l8 5 8-5V7zm0 2.8V17h16V9.8l-8 5z"/></svg>
        dwayne@tqnetworks.com.au
      </li>
      <li>
        <svg viewBox="0 0 24 24" aria-hidden="true"><circle cx="12" cy="12" r="10"/></svg>
        www.tqnetworks.com.au
      </li>
    </ul>

    <div class="person">
      <div class="person-name">Dwayne Falstrup</div>
      <div class="person-title">Director</div>
    </div>
    <div class="accent-bar"></div>
  </section>

</main>
</body>
</html>
```